Japanese Rice Food Package Label

- We are launching Japanese food products to the outdoor community.
- Made in Japan
- We will have multiple flavors of rice but want to keep the package label almost the same and only replace the flavor text (e.g., Mixed Rice, Curry Rice, etc)
- We like simple designs inspired by Japan.
- Label size: 105 mm x148 mm
- Our brand: YURATO https://yurato.co/
- Video message: https://www.clipvane.com/share/4b7e19d0a3c65f2e8d1a7b30c9e5f412

```html
<!DOCTYPE html>
<html lang="en">
<head>
<meta charset="UTF-8">
<title>YURATO Rice Labels</title>
<link href="https://fonts.googleapis.com/css2?family=Poppins:wght@500;600;700;800&display=swap" rel="stylesheet">
<style>
  :root {
    --bg: #f2efea;
    --paper: #ffffff;
    --wave: #eeeeee;
    --ink: #141414;
    --teal: #16b5b8;
    --curry: #f39220;
    --mixed: #e61e2a;
    --bowl: #5b3a29;
    --rice: #f4f6f7;
  }
  * { box-sizing: border-box; margin: 0; padding: 0; }
  html, body { width: 1200px; height: 722px; overflow: hidden; }
  body {
    background: var(--bg);
    font-family: "Poppins", sans-serif;
    color: var(--ink);
    position: relative;
  }
  .label {
    position: absolute;
    top: 168px;
    width: 540px;
    height: 385px;
    background: var(--paper);
    overflow: hidden;
    box-shadow: 0 2px 10px rgba(0,0,0,0.08);
  }
  .label--curry { left: 40px; --accent: var(--curry); }
  .label--mixed { left: 620px; --accent: var(--mixed); }

  .label__pattern {
    position: absolute; inset: 0 0 36px 0;
    background: linear-gradient(180deg, #fafafa, var(--wave));
  }
  .label__art {
    position: absolute;
    left: 282px; top: 12px;
    width: 250px; height: 330px;
    border-radius: 50%;
    background:
      radial-gradient(circle at 48% 52%, var(--rice) 0 26%, var(--bowl) 27% 40%, transparent 41%),
      var(--accent);
  }
  .label__brand {
    position: absolute;
    right: 14px; top: 12px;
    writing-mode: vertical-rl;
    font-weight: 800;
    font-size: 36px;
    letter-spacing: 1px;
    line-height: 1;
    color: var(--ink);
  }
  .label__title {
    position: absolute;
    left: 10px; top: 14px;
    font-weight: 800;
    font-size: 70px;
    line-height: 0.98;
    letter-spacing: 1px;
    color: var(--accent);
  }
  .label__tagline {
    position: absolute;
    left: 12px; top: 162px;
    font-weight: 600;
    font-size: 14px;
    line-height: 1.3;
  }
  .label__subline {
    position: absolute;
    left: 16px; top: 246px;
    font-weight: 600;
    font-size: 18px;
  }
  .steps {
    position: absolute;
    left: 14px; top: 280px;
    display: flex; gap: 8px;
    list-style: none;
  }
  .step {
    width: 66px; height: 62px;
    background: var(--teal);
    border-radius: 10px;
    display: flex; flex-direction: column; align-items: center; justify-content: center;
    color: #fff;
    font-weight: 600;
    font-size: 8px;
    line-height: 1.05;
    text-align: center;
  }
  .step svg { width: 30px; height: 26px; margin-bottom: 3px; }
  .label__band {
    position: absolute;
    left: 0; right: 0; bottom: 0;
    height: 36px;
    background: var(--ink);
    color: #fff;
    display: flex; justify-content: space-between; align-items: center;
    padding: 0 14px;
    font-weight: 600;
    font-size: 12px;
  }
</style>
</head>
<body>

<section class="label label--curry">
  <div class="label__pattern" role="img" aria-label="Soft grey Japanese wave background pattern"></div>
  <div class="label__art" role="img" aria-label="Cute rice bowl mascot with chopsticks over an orange brush-stroke circle"></div>
  <div class="label__brand">YURATO</div>
  <h1 class="label__title">CURRY<br>RICE</h1>
  <p class="label__tagline">LOREM IPSUM LOREM IPSUM<br>LOREM IPSUM LOREM IPSUM</p>
  <p class="label__subline">LOREM IPSUM LOREM IPSUM</p>
  <ul class="steps">
    <li class="step">
      <svg viewBox="0 0 30 26" fill="none" stroke="#111" stroke-width="2"><rect x="2" y="4" width="26" height="18" rx="3"/><circle cx="12" cy="13" r="5"/><line x1="9" y1="16" x2="15" y2="10"/><circle cx="24" cy="9" r="1"/><circle cx="24" cy="13" r="1"/></svg>
      NO<br>MICROWAVE
    </li>
    <li class="step">
      <svg viewBox="0 0 30 26" fill="#111"><path d="M9 10 Q15 3 21 10 L23 22 H7 Z"/><path d="M3 12 L8 16 L7 19 Z"/><circle cx="15" cy="5" r="2"/></svg>
      JUST ADD<br>HOT WATER
    </li>
    <li class="step">
      <svg viewBox="0 0 30 26" fill="none" stroke="#111" stroke-width="2"><circle cx="15" cy="13" r="11"/><polyline points="15,6 15,13 20,13"/></svg>
      WAIT<br>15 MIN
    </li>
    <li class="step">
      <svg viewBox="0 0 30 26" fill="none" stroke="#111" stroke-width="2.5" stroke-linecap="round"><line x1="7" y1="3" x2="23" y2="24"/><line x1="23" y1="3" x2="7" y2="24"/></svg>
      READY<br>TO EAT
    </li>
  </ul>
  <div class="label__band"><span>NET. WT. 0.24oz (71g)</span><span>MADE IN JAPAN</span></div>
</section>

<section class="label label--mixed">
  <div class="label__pattern" role="img" aria-label="Soft grey Japanese wave background pattern"></div>
  <div class="label__art" role="img" aria-label="Cute rice bowl mascot with chopsticks over a red brush-stroke circle"></div>
  <div class="label__brand">YURATO</div>
  <h1 class="label__title">MIXED<br>RICE</h1>
  <p class="label__tagline">LOREM IPSUM LOREM IPSUM<br>LOREM IPSUM LOREM IPSUM</p>
  <p class="label__subline">LOREM IPSUM LOREM IPSUM</p>
  <ul class="steps">
    <li class="step">
      <svg viewBox="0 0 30 26" fill="none" stroke="#111" stroke-width="2"><rect x="2" y="4" width="26" height="18" rx="3"/><circle cx="12" cy="13" r="5"/><line x1="9" y1="16" x2="15" y2="10"/><circle cx="24" cy="9" r="1"/><circle cx="24" cy="13" r="1"/></svg>
      NO<br>MICROWAVE
    </li>
    <li class="step">
      <svg viewBox="0 0 30 26" fill="#111"><path d="M9 10 Q15 3 21 10 L23 22 H7 Z"/><path d="M3 12 L8 16 L7 19 Z"/><circle cx="15" cy="5" r="2"/></svg>
      JUST ADD<br>HOT WATER
    </li>
    <li class="step">
      <svg viewBox="0 0 30 26" fill="none" stroke="#111" stroke-width="2"><circle cx="15" cy="13" r="11"/><polyline points="15,6 15,13 20,13"/></svg>
      WAIT<br>15 MIN
    </li>
    <li class="step">
      <svg viewBox="0 0 30 26" fill="none" stroke="#111" stroke-width="2.5" stroke-linecap="round"><line x1="7" y1="3" x2="23" y2="24"/><line x1="23" y1="3" x2="7" y2="24"/></svg>
      READY<br>TO EAT
    </li>
  </ul>
  <div class="label__band"><span>NET. WT. 0.24oz (71g)</span><span>MADE IN JAPAN</span></div>
</section>

</body>
</html>
```